Brava Stone Oven Kitchen (restaurant)

Restaurant with a cool vibe.
We need a refresh of existing site. Appealing to a hip crowd of 25 or older age bracket (mid price to high small town). Constant changes food and cocktail menu. A vibing atmosphere with jazz funk hip music.
Must be able to scale for any device… phone/mobile device super important.
Instagram: @Brava.Linwell
Website: bravalinwell.example

Target Market(s)

25-55 age group

Number of Pages Required

1 page

Font styles to use
Sans Serif

Requirements
Must have
• Simple to navigate. Simplicity is the key to all sophistication.

Links/Buttons
Menu
Gift Cards
Reservations
Take Out
Contact Us
Should not have
• Please, nothing generic looking… no cookie cutter look. Originality

```html
<!DOCTYPE html>
<html lang="en">
<head>
<meta charset="utf-8">
<title>Brava Stone Oven Kitchen</title>
<link href="https://fonts.googleapis.com/css2?family=Roboto:wght@400;500;700;900&display=swap" rel="stylesheet">
<style>
:root{
  --red:#e30613;
  --ink:#1e1e1e;
  --ink-deep:#161616;
  --paper:#f3f3f3;
  --text:#ffffff;
  --muted:#d8d8d8;
  --field:#ffffff;
}
*{box-sizing:border-box;margin:0;padding:0}
html,body{width:1200px;height:3000px;overflow:hidden}
body{background:var(--paper);font-family:"Roboto",sans-serif;color:var(--text)}
.page{position:absolute;left:186px;top:0;width:828px;height:3000px;background:var(--ink);overflow:hidden}
.abs{position:absolute}
.photo{position:absolute;border-radius:2px}
.glow{position:absolute;border-radius:50%;pointer-events:none}

/* hero and nav */
.hero{position:absolute;left:0;top:0;width:828px;height:421px;background:linear-gradient(160deg,#3b2e24 0%,#6a5440 35%,#574433 60%,#2a211b 100%)}
.hero-shade{position:absolute;inset:0;background:linear-gradient(90deg,rgba(0,0,0,.5) 0%,rgba(0,0,0,.15) 60%,rgba(0,0,0,.3) 100%)}
.nav{position:absolute;left:0;top:0;width:828px;height:57px;background:rgba(20,20,20,.75)}
.brand{position:absolute;text-align:center;font-weight:700;letter-spacing:2px;color:var(--text)}
.brand small{display:block;font-weight:700;letter-spacing:.3px}
.nav a{position:absolute;top:24px;font-size:10px;color:var(--text);text-decoration:none}
.btn{position:absolute;background:var(--red);color:var(--text);font-weight:500;border-radius:14px;text-align:center;text-transform:uppercase;text-decoration:none}

.hero-kicker{position:absolute;left:47px;top:163px;font-size:31px;font-weight:400;line-height:36px}
.hero-rule{position:absolute;left:178px;top:181px;width:211px;height:2px;background:var(--text)}
.hero-title{position:absolute;left:47px;top:198px;font-size:34px;font-weight:700;letter-spacing:.3px;line-height:40px}
.hero-copy{position:absolute;left:47px;top:251px;width:365px;font-size:11.5px;line-height:13.3px}

/* section headings */
.h2{position:absolute;left:0;right:0;text-align:center;font-size:31px;font-weight:700;text-transform:uppercase;line-height:36px}
.h2 .hot{color:var(--red)}
.bars{position:absolute;height:3px}
.bars i{position:absolute;top:0;height:3px;background:var(--red)}
.lede{position:absolute;left:140px;width:548px;text-align:center;font-size:11.5px;line-height:13.3px}

/* about */
.about-title{position:absolute;left:441px;top:514px;font-size:31px;font-weight:700;line-height:36px}
.about-copy{position:absolute;left:440px;top:570px;width:302px;font-size:11.5px;line-height:13.3px}

/* menu */
.dish{position:absolute;box-shadow:6px 8px 10px rgba(0,0,0,.6)}
.dish-label{position:absolute;width:180px;text-align:center;font-size:14px;font-weight:500}
.arrows{position:absolute;width:86px;height:14px}

/* testimonials */
.quote{position:absolute;width:245px;height:136px;border:2px solid var(--text);border-radius:3px;padding:27px 14px 0}
.quote p{font-size:9.3px;line-height:11px;text-indent:52px}
.quote .qm{position:absolute;left:28px;top:13px;width:27px;height:22px}
.quote h4{font-size:10px;font-weight:500;margin-top:6px}
.quote .tick{width:40px;height:2px;background:var(--red);margin-top:3px}

/* blog */
.post{position:absolute;width:152px}
.post .pic{height:110px}
.post h5{font-size:10.5px;font-weight:700;margin-top:14px}
.post p{font-size:9.3px;line-height:11px;color:var(--muted)}
.post .more{display:block;text-align:right;font-size:9.3px;margin-top:6px;margin-right:4px;color:var(--muted)}

/* hours */
.hours-h{position:absolute;font-size:22px;font-weight:700;text-transform:uppercase}
.hours-list{position:absolute;list-style:none;font-size:14px}
.hours-list li{height:23px;position:relative;padding-left:17px;text-transform:uppercase}
.hours-list li::before{content:"";position:absolute;left:2px;top:6px;width:6px;height:6px;border-radius:50%;background:var(--red)}

/* contact */
.touch-h{position:absolute;left:101px;top:2574px;font-size:20px;font-weight:700}
.touch-row{position:absolute;left:101px;font-size:13px;display:flex;align-items:center;gap:11px}
.touch-row svg{width:16px;height:16px}
.field{position:absolute;background:var(--field);color:#8a8a8a;font-size:7.5px;padding:9px 9px;text-transform:uppercase}

/* footer */
.footer{position:absolute;left:0;top:2805px;width:828px;height:195px;background:linear-gradient(180deg,#3a2b22 0%,#2d211a 100%)}
.footer-shade{position:absolute;inset:0;background:rgba(0,0,0,.6)}
.foot-copy{position:absolute;left:190px;top:2882px;width:448px;text-align:center;font-size:10px;line-height:12px}
.foot-links a{position:absolute;top:2940px;font-size:10px;color:var(--text);text-decoration:none}
.foot-rule{position:absolute;left:114px;top:2965px;width:599px;height:1px;background:var(--muted)}
.legal{position:absolute;left:0;right:0;top:2976px;text-align:center;font-size:8.5px}
</style>
</head>
<body>
<div class="page">

  <!-- hero -->
  <div class="hero" role="img" aria-label="Photo of the dining room with a round wooden table, glasses and stools"></div>
  <div class="hero-shade"></div>
  <nav class="nav">
    <div class="brand" style="left:40px;top:14px;font-size:21px;line-height:20px;width:130px">BRAVA<small style="font-size:7px;line-height:9px">Stone Oven Kitchen</small></div>
    <a href="#about" style="left:282px">About Us</a>
    <a href="#menu" style="left:358px">Menu</a>
    <a href="#contact" style="left:414px">Reservations</a>
    <a href="#contact" style="left:506px">Gift Cards</a>
    <a href="#hours" style="left:588px">Take Out</a>
    <a class="btn" href="#contact" style="left:721px;top:19px;width:67px;height:18px;font-size:7px;line-height:18px">Contact Us</a>
  </nav>
  <div class="hero-kicker">BRAVA</div>
  <div class="hero-rule"></div>
  <h1 class="hero-title">STONE OVEN KITCHEN</h1>
  <p class="hero-copy">Lorem ipsum dolor sit amet, consectetur adipiscing elit. Commodo sit odio laoreet sit egestas et non. consectetur adipiscing elit adipiscing elit. Commodo sit odio laoreet sit egestas et non. consectetur adipiscing elit</p>
  <a class="btn" href="#contact" style="left:45px;top:315px;width:88px;height:25px;font-size:10px;line-height:25px">Get Started</a>
  <svg class="abs" style="left:382px;top:378px" width="12" height="18" viewBox="0 0 12 18"><path d="M6 1v15M1 11l5 5 5-5" stroke="#fff" stroke-width="1.4" fill="none"/></svg>

  <!-- about -->
  <div class="glow" style="left:600px;top:560px;width:260px;height:240px;background:radial-gradient(circle,rgba(150,130,100,.35),rgba(30,30,30,0) 70%)" role="img" aria-label="Faint photo of a wrap"></div>
  <div class="photo" style="left:101px;top:475px;width:178px;height:240px;background:linear-gradient(160deg,#e2d6b8,#c9a77a 50%,#8c6b4a)" role="img" aria-label="Photo of a pressed sandwich"></div>
  <div class="photo" style="left:190px;top:504px;width:178px;height:240px;background:linear-gradient(170deg,#5a4330,#a36a36 45%,#3c3d2a);box-shadow:6px 8px 10px rgba(0,0,0,.5)" role="img" aria-label="Photo of a steak sandwich with greens"></div>
  <div class="photo" style="left:307px;top:678px;width:98px;height:85px;border-radius:50%;background:radial-gradient(circle at 50% 40%,#d9913a,#8a3f1e 60%,rgba(30,30,30,0) 72%)" role="img" aria-label="Photo of a cheeseburger"></div>
  <h2 class="about-title" id="about">ABOUT US</h2>
  <div class="bars" style="left:441px;top:556px;width:100px"><i style="left:0;width:70px"></i><i style="left:78px;width:28px"></i></div>
  <p class="about-copy">lorem ipsum dolor sit amet, consectetur adipiscing elit. commodo sit odio laoreet sit egestas et non. lorem ipsum dolor sit amet, consectetur adipiscing elit. commodo sit odio laoreet sit egestas et non. lorem ipsum dolor sit amet, consectetur adipiscing elit. commodo sit odio laoreet sit egestas et non. lorem ipsum dolor sit amet, consectetur adipiscing elit. commodo sit odio laoreet sit egestas et non.</p>
  <a class="btn" href="#menu" style="left:440px;top:684px;width:74px;height:21px;font-size:8px;line-height:21px">Learn More</a>

  <!-- menu -->
  <h2 class="h2" id="menu" style="top:832px">OUR MENU <span class="hot">ITEAM</span></h2>
  <div class="bars" style="left:360px;top:877px;width:110px"><i style="left:0;width:78px"></i><i style="left:86px;width:30px"></i></div>
  <p class="lede" style="top:890px">lorem ipsum dolor sit amet, consectetur adipiscing elit. commodo sit odio laoreet sit egestas et non. lorem ipsum dolor sit amet, consectetur adipiscing elit. commodo sit</p>
  <div class="glow" style="left:-40px;top:940px;width:200px;height:280px;background:radial-gradient(circle,rgba(140,110,80,.4),rgba(30,30,30,0) 70%)" role="img" aria-label="Faint photo of a burger"></div>
  <div class="dish" style="left:127px;top:956px;width:169px;height:216px;background:linear-gradient(170deg,#c9a06a,#6b4028 45%,#9aa86a 75%,#d8cfc0)" role="img" aria-label="Photo of a stacked roast beef sandwich"></div>
  <div class="dish" style="left:325px;top:939px;width:177px;height:240px;background:linear-gradient(165deg,#3a2a26,#c0331e 45%,#e2612c 60%,#7a1a14)" role="img" aria-label="Photo of a red cocktail with orange peel"></div>
  <div class="dish" style="left:531px;top:956px;width:167px;height:216px;background:linear-gradient(160deg,#8e8a85,#cfc6bd 40%,#b27766 65%,#5a5550)" role="img" aria-label="Photo of a plated appetizer"></div>
  <div class="dish-label" style="left:121px;top:1197px">FAST FOOD</div>
  <div class="dish-label" style="left:323px;top:1212px">COCKTAIL</div>
  <div class="dish-label" style="left:524px;top:1197px">FAST FOOD</div>
  <svg class="arrows" style="left:655px;top:1261px" viewBox="0 0 86 14"><path d="M34 7H1M7 1L1 7l6 6M52 7h33M79 1l6 6-6 6" stroke="#fff" stroke-width="1.3" fill="none"/></svg>

  <!-- testimonials -->
  <h2 class="h2" id="testimonials" style="top:1337px">OUR TESTIMO<span class="hot">NIAL</span></h2>
  <div class="bars" style="left:342px;top:1382px;width:150px"><i style="left:0;width:100px"></i><i style="left:110px;width:34px"></i></div>
  <p class="lede" style="top:1394px">lorem ipsum dolor sit amet, consectetur adipiscing elit. commodo sit odio laoreet sit egestas et non. lorem ipsum dolor sit amet, consectetur adipiscing elit. commodo sit</p>
  <div class="glow" style="left:640px;top:1410px;width:230px;height:220px;background:radial-gradient(circle,rgba(200,190,170,.35),rgba(30,30,30,0) 70%)" role="img" aria-label="Faint photo of a pasta dish"></div>
  <div class="quote" style="left:156px;top:1445px">
    <svg class="qm" viewBox="0 0 30 22"><path d="M2 20V11C2 5 5 2 11 1v4c-3 1-4 3-4 5h4v10zM17 20V11c0-6 3-9 9-10v4c-3 1-4 3-4 5h4v10z" fill="#e30613"/></svg>
    <p>lorem ipsum dolor sit amet, consectetur adipiscing elit. commodo sit odio laoreet sit egestas et non. lorem ipsum dolor sit amet, consectetur adipiscing elit. commodo sit lorem ipsum dolor sit amet, consectetur adipiscing elit. commodo sit odiom sit egestas et non. lorem ipsum dolor</p>
    <h4>MAREN OKAFOR</h4><div class="tick"></div>
  </div>
  <div class="quote" style="left:424px;top:1445px">
    <svg class="qm" viewBox="0 0 30 22"><path d="M2 20V11C2 5 5 2 11 1v4c-3 1-4 3-4 5h4v10zM17 20V11c0-6 3-9 9-10v4c-3 1-4 3-4 5h4v10z" fill="#e30613"/></svg>
    <p>lorem ipsum dolor sit amet, consectetur adipiscing elit. commodo sit odio laoreet sit egestas et non. lorem ipsum dolor sit amet, consectetur adipiscing elit. commodo sit lorem ipsum dolor sit amet, consectetur adipiscing elit. commodo sit odiom sit egestas et non. lorem ipsum dolor</p>
    <h4>MAREN OKAFOR</h4><div class="tick"></div>
  </div>
  <svg class="arrows" style="left:655px;top:1628px" viewBox="0 0 86 14"><path d="M34 7H1M7 1L1 7l6 6M52 7h33M79 1l6 6-6 6" stroke="#fff" stroke-width="1.3" fill="none"/></svg>

  <!-- blog -->
  <h2 class="h2" id="blog" style="top:1686px">OUR BLOG\<span class="hot">NEWS</span></h2>
  <p class="lede" style="top:1743px">lorem ipsum dolor sit amet, consectetur adipiscing elit. commodo sit odio laoreet sit egestas et non. lorem ipsum dolor sit amet, consectetur adipiscing elit. commodo sit</p>
  <div class="glow" style="left:-30px;top:1760px;width:230px;height:300px;background:radial-gradient(circle,rgba(170,60,50,.35),rgba(30,30,30,0) 70%)" role="img" aria-label="Faint photo of cocktails and strawberries"></div>
  <div class="post" style="left:168px;top:1786px">
    <div class="pic" style="background:linear-gradient(160deg,#4a4038,#a8917a 50%,#3a3530)" role="img" aria-label="Photo of the restaurant counter"></div>
    <h5>lorem ipsum</h5>
    <p>lorem ipsum dolor sit amet,conse dipiscing elit. commodo sit odio lao reet sit egestas et non. lorem ipsum dolor sit amet,</p>
    <span class="more">Read More</span>
  </div>
  <div class="post" style="left:338px;top:1786px">
    <div class="pic" style="background:linear-gradient(170deg,#c07a3a,#8a9a4a 55%,#5a4030)" role="img" aria-label="Photo of a burger with guacamole"></div>
    <h5>lorem ipsum</h5>
    <p>lorem ipsum dolor sit amet,conse dipiscing elit. commodo sit odio lao reet sit egestas et non. lorem ipsum dolor sit amet,</p>
    <span class="more">Read More</span>
  </div>
  <div class="post" style="left:506px;top:1786px">
    <div class="pic" style="background:linear-gradient(160deg,#3a332e,#8a6e5c 50%,#2e2a27)" role="img" aria-label="Photo of a group of guests at the restaurant"></div>
    <h5>lorem ipsum</h5>
    <p>lorem ipsum dolor sit amet,conse dipiscing elit. commodo sit odio lao reet sit egestas et non. lorem ipsum dolor sit amet,</p>
    <span class="more">Read More</span>
  </div>
  <a class="btn" href="#blog" style="left:376px;top:2014px;width:74px;height:20px;font-size:8px;line-height:20px">View More</a>

  <!-- hours -->
  <div class="glow" style="left:560px;top:2060px;width:300px;height:300px;background:radial-gradient(circle,rgba(170,120,70,.35),rgba(30,30,30,0) 70%)" role="img" aria-label="Faint photo of a pizza"></div>
  <h3 class="hours-h" id="hours" style="left:102px;top:2126px">CANADA DAY HOURS!</h3>
  <div class="bars" style="left:102px;top:2158px;width:130px"><i style="left:0;width:132px"></i></div>
  <ul class="hours-list" style="left:102px;top:2167px">
    <li>Thursday, July 1st&nbsp; - &nbsp;Open</li>
    <li>Friday, July 2nd&nbsp; - &nbsp;Open</li>
    <li>Saturday, July 3rd&nbsp; - &nbsp;Open</li>
    <li>Sunday, July 4th&nbsp; - &nbsp;Closed</li>
  </ul>
  <h3 class="hours-h" style="left:102px;top:2273px">TAKEOUT &amp; KITCHEN HOURS</h3>
  <div class="bars" style="left:102px;top:2304px;width:130px"><i style="left:0;width:132px"></i></div>
  <ul class="hours-list" style="left:102px;top:2323px">
    <li>Thursday to Sunday</li>
    <li>12:00PM - 8:00PM</li>
  </ul>
  <h3 class="hours-h" style="left:448px;top:2123px">OUTDOOR DINING HOURS</h3>
  <div class="bars" style="left:448px;top:2155px;width:200px"><i style="left:0;width:200px"></i></div>
  <ul class="hours-list" style="left:448px;top:2167px">
    <li>Our courtyard is open!</li>
    <li>Thursday to Sunday</li>
    <li>12:00PM - 9:00PM</li>
  </ul>

  <!-- contact -->
  <h2 class="h2" id="contact" style="top:2458px">OUR CONTACT US</h2>
  <div class="bars" style="left:357px;top:2502px;width:120px"><i style="left:0;width:80px"></i><i style="left:88px;width:28px"></i></div>
  <div class="glow" style="left:-10px;top:2540px;width:380px;height:240px;background:radial-gradient(ellipse,rgba(140,130,115,.3),rgba(30,30,30,0) 70%)" role="img" aria-label="Faint photo of a plated dish"></div>
  <h3 class="touch-h">GET IN TOUCH</h3>
  <div class="touch-row" style="top:2612px">
    <svg viewBox="0 0 16 16"><path d="M3 1l3 3-1.5 2c1 2 3 4 5 5L11.5 9.5l3 3L13 15C7 14 2 9 1 3z" fill="#e30613"/></svg>555-010-4821</div>
  <div class="touch-row" style="top:2645px">
    <svg viewBox="0 0 16 16"><rect x="1.5" y="3.5" width="13" height="9" fill="none" stroke="#e30613" stroke-width="1.2"/><path d="M1.5 3.5l6.5 5 6.5-5M1.5 12.5l5-4.5M14.5 12.5l-5-4.5" fill="none" stroke="#e30613" stroke-width="1.2"/></svg>hello@bravalinwell.example</div>
  <div class="touch-row" style="top:2676px">
    <svg viewBox="0 0 16 16"><path d="M15 1L1 7l6 2 2 6z" fill="#e30613"/></svg>Street no 4 near the market, Linwell USA</div>
  <div class="field" style="left:445px;top:2560px;width:152px;height:28px">Name</div>
  <div class="field" style="left:607px;top:2560px;width:153px;height:28px">Last Name</div>
  <div class="field" style="left:445px;top:2598px;width:152px;height:28px">Phone</div>
  <div class="field" style="left:607px;top:2598px;width:153px;height:28px">Email</div>
  <div class="field" style="left:445px;top:2636px;width:315px;height:73px">Message</div>
  <a class="btn" href="#contact" style="left:565px;top:2727px;width:76px;height:20px;font-size:8px;line-height:20px">Submit</a>

  <!-- footer -->
  <footer class="footer" role="img" aria-label="Photo of the brick building facade"><div class="footer-shade"></div></footer>
  <div class="brand" style="left:339px;top:2830px;width:150px;font-size:23px;line-height:22px">BRAVA<small style="font-size:7.5px;line-height:9px">Stone Oven Kitchen</small></div>
  <p class="foot-copy">Lorem ipsum dolort any work amet, consectetur adipiscing elit. Pharetra donec in ut sagittis et nullam ultricies sed. Massa erat dapibus eget</p>
  <svg class="abs" style="left:372px;top:2914px" width="84" height="12" viewBox="0 0 84 12" role="img" aria-label="Social links">
    <circle cx="6" cy="6" r="5" fill="#fff"/><circle cx="29" cy="6" r="5" fill="#fff"/><circle cx="53" cy="6" r="5" fill="#fff"/><circle cx="77" cy="6" r="5" fill="#fff"/>
  </svg>
  <div class="foot-links">
    <a href="#about" style="left:200px">About Us</a>
    <a href="#menu" style="left:290px">Menu</a>
    <a href="#contact" style="left:360px">Reservations</a>
    <a href="#contact" style="left:460px">Gift Cards</a>
    <a href="#hours" style="left:552px">Take Out</a>
  </div>
  <div class="foot-rule"></div>
  <p class="legal">©2021 BRAVA , BRAVA INC ARE TRADMATE OF BRAVA FAST FOOD.</p>
</div>
</body>
</html>
```